Tri-Fold Brochure for IT Solutions Company
KORVANE, LLC
We are an IT solutions company that provides technical services to the federal government.
We would like a trifold brochure that we can deliver to potential customers that will show them a little bit about our company, services we provide, and contact information with some pictures.
Information Technology
Corporate and Government
Neat, professional, and high tech. Images that match content.
Our logo must go on the brochure. It will be provided in the Project materials.
We prefer the color scheme to be similar to our logo and website. Content & website url will be provided in the project materials draft brochure.
Here is our initial draft brochure that has our content. Please provide new, relevant, high tech graphics
Here is our logo in .png format.
Here is our logo in .ai format as well.
** UPDATED content here *** Please incorporate

```html
<!DOCTYPE html>
<html lang="en">
<head>
<meta charset="utf-8">
<title>KORVANE, LLC – Tri-Fold Brochure</title>
<link href="https://fonts.googleapis.com/css2?family=Open+Sans:wght@400;600;700;800&display=swap" rel="stylesheet">
<style>
  :root{
    --navy:#0d2a5c;
    --blue:#1a55a8;
    --sky:#3d86d6;
    --red:#c8102e;
    --ink:#2b2f36;
    --muted:#5b6470;
    --paper:#ffffff;
    --stage:#e6e9ed;
  }
  *{box-sizing:border-box;margin:0;padding:0}
  html,body{width:1200px;height:901px;overflow:hidden}
  body{background:var(--stage);font-family:"Open Sans",Arial,sans-serif;color:var(--ink);position:relative}
  .spread{position:absolute;left:20px;width:1160px;height:420px;display:grid;grid-template-columns:repeat(3,1fr);background:var(--paper);box-shadow:0 4px 14px rgba(0,0,0,.18)}
  .spread--inside{top:20px}
  .spread--outside{top:461px}
  .panel{position:relative;overflow:hidden;border-right:1px solid #e3e6ea;padding:0 0 70px}
  .panel:last-child{border-right:none}
  .panel__body{padding:12px 26px 0}
  .photo{display:block;width:100%}
  .photo--lock{height:125px;background:linear-gradient(135deg,#0b3a2e,#1e7a4a 45%,#0e3f7a)}
  .photo--network{height:125px;background:linear-gradient(135deg,#dce8f5,#6fa4de 55%,#1a55a8)}
  .photo--code{height:70px;margin-top:10px;background:linear-gradient(90deg,#0d2a5c,#3d86d6)}
  .photo--servers{position:absolute;left:26px;right:26px;bottom:78px;height:112px;background:linear-gradient(180deg,#1c1f26,#3c424d 60%,#15171c)}
  .photo--fingerprint{position:absolute;left:0;right:0;bottom:70px;height:150px;background:radial-gradient(circle at 50% 60%,#3d86d6,#0d2a5c 70%)}
  .heading{display:flex;align-items:baseline;gap:2px;color:var(--navy);font-weight:700;font-size:18px;margin-bottom:6px}
  .heading__initial{color:var(--red);font-size:26px;font-weight:800;font-style:normal}
  .text{font-size:9.5px;line-height:1.5;color:var(--muted);margin-bottom:7px}
  .list{list-style:none;font-size:9.5px;line-height:1.6;color:var(--ink)}
  .list li{padding-left:12px;position:relative}
  .list li::before{content:"";position:absolute;left:0;top:5px;width:6px;height:6px;background:var(--red);border-radius:50%}
  .list--cols{columns:2}
  .band{position:absolute;left:0;right:0;bottom:0;height:70px}
  .contact{margin-top:8px}
  .contact__line{font-size:9.5px;line-height:1.5;color:var(--ink)}
  .website{position:absolute;left:0;right:0;bottom:14px;text-align:center;font-weight:700;font-size:13px;color:#fff;z-index:2}
  .cover{padding:0}
  .brand{display:flex;align-items:center;justify-content:center;gap:10px;padding:38px 20px 10px}
  .brand__mark{width:26px;height:26px;border-radius:50%;background:var(--red)}
  .brand__name{font-weight:800;font-size:30px;color:var(--navy);letter-spacing:1px}
  .cover__intro{font-size:11px;line-height:1.55;color:var(--muted);text-align:center;padding:6px 36px}
  .tagline{position:absolute;left:0;right:0;bottom:18px;text-align:center;font-weight:700;font-size:20px;color:#fff;z-index:2}
</style>
</head>
<body>

<section class="spread spread--inside" aria-label="Brochure inside">
  <article class="panel">
    <div class="photo photo--lock" role="img" aria-label="Digital padlock over circuit board"></div>
    <div class="panel__body">
      <h2 class="heading"><span class="heading__initial">C</span>yber Security</h2>
      <p class="text">KORVANE provides certified cyber security professionals to safeguard federal systems and data. Our staff brings deep experience in risk assessment, continuous monitoring and incident response.</p>
      <ul class="list">
        <li>Risk and Threat Assessment</li>
        <li>Network Intrusion Detection</li>
        <li>Vulnerability Management</li>
        <li>Security Compliance Audits</li>
        <li>Incident Response Planning</li>
      </ul>
    </div>
    <svg class="band" viewBox="0 0 386 70" preserveAspectRatio="none" aria-hidden="true">
      <path d="M0 28 C120 0 260 50 386 18 L386 70 L0 70Z" fill="var(--blue)"/>
      <path d="M0 28 C120 0 260 50 386 18" stroke="var(--red)" stroke-width="4" fill="none"/>
    </svg>
  </article>

  <article class="panel">
    <div class="panel__body" style="padding-top:22px">
      <h2 class="heading"><span class="heading__initial">S</span>oftware Engineering</h2>
      <p class="text">KORVANE, LLC delivers software engineers experienced in the full development life cycle, from requirements and design to testing, deployment and long-term support of mission applications.</p>
      <ul class="list list--cols">
        <li>Java</li><li>.NET</li><li>C#</li><li>Python</li><li>SQL</li>
        <li>Agile</li><li>DevOps</li><li>Testing</li><li>Web Services</li><li>Mobile</li>
      </ul>
      <div class="photo photo--code" role="img" aria-label="Software code on screen"></div>
      <p class="text" style="margin-top:8px">Our teams build secure, scalable solutions that meet agency standards and deliver measurable value on schedule.</p>
    </div>
    <svg class="band" viewBox="0 0 386 70" preserveAspectRatio="none" aria-hidden="true">
      <path d="M0 18 C130 50 260 0 386 28 L386 70 L0 70Z" fill="var(--blue)"/>
      <path d="M0 18 C130 50 260 0 386 28" stroke="var(--red)" stroke-width="4" fill="none"/>
    </svg>
  </article>

  <article class="panel">
    <div class="photo photo--network" role="img" aria-label="Connected computer network"></div>
    <div class="panel__body">
      <h2 class="heading"><span class="heading__initial">S</span>ystems Engineering</h2>
      <p class="text">We design, integrate and maintain complex systems that keep government operations running. Our engineers align technology with mission goals and budgets.</p>
      <ul class="list">
        <li>Requirements Analysis</li>
        <li>System Integration</li>
        <li>Architecture Design</li>
        <li>Lifecycle Support</li>
      </ul>
    </div>
    <svg class="band" viewBox="0 0 386 70" preserveAspectRatio="none" aria-hidden="true">
      <path d="M0 28 C120 0 260 50 386 18 L386 70 L0 70Z" fill="var(--blue)"/>
      <path d="M0 28 C120 0 260 50 386 18" stroke="var(--red)" stroke-width="4" fill="none"/>
    </svg>
  </article>
</section>

<section class="spread spread--outside" aria-label="Brochure outside">
  <article class="panel">
    <div class="panel__body" style="padding-top:22px">
      <h2 class="heading"><span class="heading__initial">S</span>ystems Administration</h2>
      <p class="text">Our administrators keep servers, networks and workstations secure, patched and available around the clock, supporting thousands of users across federal sites.</p>
      <ul class="list">
        <li>Windows and Linux Servers</li>
        <li>Active Directory</li>
        <li>Backup and Recovery</li>
        <li>Help Desk Support</li>
        <li>Patch Management</li>
        <li>Network Monitoring</li>
      </ul>
    </div>
    <div class="photo photo--servers" role="img" aria-label="Server racks in a data center"></div>
    <svg class="band" viewBox="0 0 386 70" preserveAspectRatio="none" aria-hidden="true">
      <path d="M0 28 C120 0 260 50 386 18 L386 70 L0 70Z" fill="var(--blue)"/>
      <path d="M0 28 C120 0 260 50 386 18" stroke="var(--red)" stroke-width="4" fill="none"/>
    </svg>
  </article>

  <article class="panel">
    <div class="panel__body" style="padding-top:22px">
      <h2 class="heading"><span class="heading__initial">V</span>irtualization</h2>
      <p class="text">Our virtualization staff enables agencies to consolidate servers, reduce costs and improve resilience. KORVANE plans, builds and manages virtual environments for every need.</p>
      <ul class="list">
        <li>VDI Infrastructure Solutions</li>
        <li>Cloud Migration</li>
        <li>Server Consolidation</li>
        <li>Storage Virtualization</li>
        <li>Capacity Planning</li>
      </ul>
      <div class="contact">
        <h2 class="heading"><span class="heading__initial">C</span>ontact Us</h2>
        <p class="contact__line">1450 Meridian Parkway, Suite 210</p>
        <p class="contact__line">Columbia, MD 21045</p>
        <p class="contact__line">P: 410-555-0184</p>
        <p class="contact__line">info@korvanetech.com</p>
      </div>
    </div>
    <svg class="band" viewBox="0 0 386 70" preserveAspectRatio="none" aria-hidden="true">
      <path d="M0 18 C130 50 260 0 386 28 L386 70 L0 70Z" fill="var(--blue)"/>
      <path d="M0 18 C130 50 260 0 386 28" stroke="var(--red)" stroke-width="4" fill="none"/>
    </svg>
    <p class="website">www.korvanetech.com</p>
  </article>

  <article class="panel cover">
    <div class="brand">
      <span class="brand__mark" aria-hidden="true"></span>
      <span class="brand__name">KORVANE, LLC</span>
    </div>
    <p class="cover__intro">KORVANE, LLC is an IT solutions company that provides technical services to the federal government across Cyber Security, Software Engineering, Systems Engineering and Virtualization.</p>
    <div class="photo photo--fingerprint" role="img" aria-label="Digital fingerprint scan"></div>
    <svg class="band" viewBox="0 0 386 70" preserveAspectRatio="none" aria-hidden="true">
      <path d="M0 28 C120 0 260 50 386 18 L386 70 L0 70Z" fill="var(--navy)"/>
      <path d="M0 28 C120 0 260 50 386 18" stroke="var(--red)" stroke-width="4" fill="none"/>
    </svg>
    <p class="tagline">Use Your KORVANE!</p>
  </article>
</section>

</body>
</html>
```